Corvenix Business Card

Our mission is to craft high value solutions combining consulting and edge technologies for helping big and middle sized companies in the Digital Transformation Process that they must face. We think that this transformation will impact business processes and people skills in a new manner. Corvenix's value proposition is to collaborate with our clients for creating new competitive advantages based on technology, processes and people.
We already have a logo designed through your platform.

Industry/Entity Type

Business

```html
<!DOCTYPE html>
<html lang="en">
<head>
<meta charset="utf-8">
<title>Corvenix Business Card</title>
<link rel="stylesheet" href="https://fonts.googleapis.com/css2?family=Arimo:wght@400;700&display=swap">
<style>
  :root {
    --stage: #262626;
    --card-dark: #231f20;
    --card-light: #f4f4f4;
    --ink: #1a1a1a;
    --ink-soft: #333333;
    --accent: #1e90cc;
    --mark-grey: #b5b8bb;
    --white: #ffffff;
  }
  * { margin: 0; padding: 0; box-sizing: border-box; }
  html, body {
    width: 1200px;
    height: 900px;
    overflow: hidden;
    background: var(--stage);
    font-family: "Arimo", Arial, sans-serif;
  }
  .stage {
    width: 1200px;
    height: 900px;
    display: flex;
    flex-direction: column;
    align-items: center;
    justify-content: center;
    gap: 60px;
  }
  .card {
    width: 740px;
    height: 320px;
    position: relative;
    box-shadow: 0 12px 30px rgba(0,0,0,0.5);
  }

  /* Front */
  .card-front {
    background: var(--card-dark);
    display: flex;
    align-items: center;
    justify-content: center;
    gap: 22px;
  }
  .brand-dot {
    width: 70px;
    height: 70px;
    border-radius: 50%;
    background: var(--accent);
  }
  .brand-name {
    color: var(--white);
    font-size: 58px;
    font-weight: 400;
    letter-spacing: 2px;
    text-transform: uppercase;
  }

  /* Back */
  .card-back {
    background: var(--card-light);
    color: var(--ink);
  }
  .back-brand {
    position: absolute;
    left: 300px;
    top: 52px;
    display: flex;
    align-items: center;
    gap: 12px;
  }
  .back-brand .brand-dot { width: 44px; height: 44px; }
  .back-brand .brand-name {
    color: var(--accent);
    font-size: 30px;
    text-transform: none;
    letter-spacing: 0;
  }
  .social {
    position: absolute;
    right: 70px;
    top: 62px;
    display: flex;
    gap: 6px;
  }
  .social span {
    width: 22px;
    height: 22px;
    background: var(--ink);
    border-radius: 3px;
  }
  .holder {
    position: absolute;
    left: 60px;
    top: 150px;
  }
  .holder-name {
    font-size: 40px;
    font-weight: 400;
    line-height: 1;
  }
  .holder-role {
    font-size: 15px;
    margin-top: 4px;
    margin-left: 10px;
    color: var(--ink-soft);
  }
  .contact {
    position: absolute;
    font-size: 16px;
    color: var(--ink-soft);
  }
  .contact b {
    color: var(--accent);
    font-weight: 400;
    margin-right: 4px;
  }
  .contact-phone { left: 90px; top: 256px; }
  .contact-email { left: 330px; top: 210px; }
  .contact-web { right: 70px; top: 150px; }
</style>
</head>
<body>
<main class="stage">
  <section class="card card-front" aria-label="Card front">
    <span class="brand-dot" aria-hidden="true"></span>
    <span class="brand-name">Corvenix</span>
  </section>

  <section class="card card-back" aria-label="Card back">
    <div class="back-brand">
      <span class="brand-dot" aria-hidden="true"></span>
      <span class="brand-name">Corvenix</span>
    </div>
    <div class="social" aria-label="Social profiles">
      <span></span><span></span><span></span><span></span>
    </div>
    <div class="holder">
      <p class="holder-name">Your Name</p>
      <p class="holder-role">Company Position</p>
    </div>
    <p class="contact contact-web"><b>W:</b>www.corvenix.com</p>
    <p class="contact contact-email"><b>E:</b>youremail@domain.com</p>
    <p class="contact contact-phone"><b>P:</b>000 123 4555</p>
  </section>
</main>
</body>
</html>
```